Human Resource Consultant's Website needs an Updated Look

I'm an HR Consultant based in Denver that caters to small business owners. I like my logo, and the existing content (though open to editorial suggestions) but would like to reformat my site and possibly update graphics. I want to be able to manage content moving forward. PLWTAdvisory.com

Target Market(s)

Small business owners with 10-500 employees in Metro Denver

Coding

Coded - Design and coding required

Font styles to use
Other font styles liked:
• Closer to existing font but open to suggestions

Colors

Designer to choose colors to be used in the design.

Requirements
Must have
• Links on landing page to other pages
• Visual appeal to younger demographic found in the small to medium sized business owner
• Scroll down rather than use the clunky "ladder" tabs I see now
• Color palate that compliments logo
Nice to have
• Pages that scroll down, links to page content on the first page,
Should not have
• Hate the standard employee-employer photos on most HR websites. Would prefer to use illustrations over the typical photos

```html
<!DOCTYPE html>
<html lang="en">
<head>
<meta charset="utf-8">
<title>PLWT Advisory</title>
<link href="https://fonts.googleapis.com/css2?family=Questrial&family=Montserrat:wght@600;700&display=swap" rel="stylesheet">
<style>
:root{
  --green:#a6c32a;
  --navy:#1d4f7c;
  --ink:#1b1b1b;
  --muted:#9a9a9a;
  --line:#e4e4e4;
  --hero-a:#6e7378;
  --hero-b:#b49b7c;
  --footer-a:#1e5b8c;
  --footer-b:#1a91b3;
  --map:#e6e7e8;
}
*{box-sizing:border-box;margin:0;padding:0}
html,body{width:1200px;height:2525px;overflow:hidden;background:#fff}
body{position:relative;font-family:"Questrial",sans-serif;color:var(--ink)}
.abs{position:absolute}
.btn{position:absolute;background:var(--green);color:#fff;font-family:"Montserrat",sans-serif;font-weight:600;font-size:12px;display:flex;align-items:center;justify-content:center}
.btn-outline{background:#fff;color:var(--green);border:1px solid var(--green)}

/* header */
.site-header{position:absolute;left:0;top:0;width:1200px;height:104px;background:#fff}
.brand{left:156px;top:18px;display:flex;align-items:center;gap:14px}
.brand-mark{width:50px;height:50px;border-radius:50%;background:var(--navy)}
.brand-name{font-size:30px;color:var(--navy);line-height:1}
.brand-tag{font-size:11px;color:var(--navy);margin-top:6px}
.call{left:750px;top:22px;font-family:"Montserrat",sans-serif;font-weight:600;font-size:14px;color:var(--green);display:flex;align-items:center;gap:8px}
.call b{color:var(--navy);font-weight:600}
.social{display:flex;gap:8px}
.social span{width:24px;height:24px;border-radius:50%;border:1.5px solid var(--green)}
.social span.on{background:var(--green)}
.header-social{left:950px;top:20px}
.nav{left:569px;top:64px;display:flex;gap:0;font-family:"Montserrat",sans-serif;font-weight:600;font-size:13px}
.nav a{text-decoration:none;color:var(--ink);position:absolute;white-space:nowrap}
.nav a.active{color:var(--green)}

/* hero */
.hero{left:0;top:104px;width:1200px;height:519px;background:linear-gradient(180deg,var(--hero-a) 0%,#7e8184 62%,var(--hero-b) 63%,#a88c6d 100%)}
.hero-art{position:absolute;left:560px;top:40px;width:440px;height:440px;background:radial-gradient(circle at 50% 55%,#e7b53a 0%,#c7566b 35%,#4f8fb0 60%,rgba(110,115,120,0) 75%)}
.hero h1{position:absolute;left:156px;top:170px;font-weight:400;font-size:29px;line-height:36px;color:#fff}
.hero h1 strong{font-family:"Montserrat",sans-serif;font-weight:700}
.hero .btn{left:156px;top:312px;width:128px;height:32px}
.arrow{position:absolute;width:32px;height:32px;border-radius:50%;display:flex;align-items:center;justify-content:center}
.arrow-left{left:50px;top:244px;border:1.5px solid #fff}
.arrow-right{left:1118px;top:244px;background:#1a91b3}

/* approach */
.eyebrow{font-family:"Montserrat",sans-serif;font-weight:600;font-size:13px;color:var(--navy)}
.approach-label{left:156px;top:727px}
.approach-title{left:156px;top:762px;width:400px;font-weight:400;font-size:25px;line-height:28px}
.body-copy{font-size:12.5px;line-height:20px;color:var(--muted)}
.approach-p1{left:156px;top:876px;width:380px}
.approach-sub{left:156px;top:952px;font-family:"Montserrat",sans-serif;font-weight:600;font-size:13px;color:var(--green)}
.approach-p2{left:156px;top:987px;width:430px}
.approach .btn{left:156px;top:1094px;width:144px;height:31px}
.portrait{left:675px;top:703px;width:368px;height:448px;background:linear-gradient(160deg,#b0553c 0%,#9b4a36 40%,#2b4036 75%,#1e2b27 100%)}

/* services */
.services-label{left:0;width:1200px;top:1229px;text-align:center}
.tabs{left:156px;top:1282px;width:887px;height:40px;border-bottom:1px solid var(--line);display:flex}
.tab{flex:1;display:flex;align-items:center;justify-content:center;font-family:"Montserrat",sans-serif;font-weight:600;font-size:14px;position:relative}
.tab.active{background:var(--green);color:#fff}
.tab.active::after{content:"";position:absolute;bottom:-9px;left:50%;margin-left:-9px;border-left:9px solid transparent;border-right:9px solid transparent;border-top:9px solid var(--green)}
.topics-title{left:156px;top:1388px;width:400px;font-weight:400;font-size:25px;line-height:29px}
.topics{left:156px;top:1469px;list-style:none;font-size:12.5px;line-height:19.4px;color:var(--muted)}
.topics li{display:flex;align-items:center;gap:8px}
.topics .btn{left:0}
.services-btn{left:156px;top:1804px;width:128px;height:31px}
.services-art{left:611px;top:1394px;width:432px;height:442px;background:linear-gradient(160deg,#6fc3dc 0%,#5bb6d3 60%,#8a4fd0 100%)}

/* map */
.map{left:0;top:1915px;width:1200px;height:281px;background:var(--map)}

/* footer */
.site-footer{left:0;top:2196px;width:1200px;height:329px;background:linear-gradient(90deg,var(--footer-a),var(--footer-b));color:#fff}
.foot-h{position:absolute;top:70px;font-family:"Montserrat",sans-serif;font-weight:600;font-size:13px;color:var(--green)}
.contact-info{position:absolute;left:156px;top:96px;font-size:12.5px;line-height:20px}
.contact-info .phone{font-family:"Montserrat",sans-serif;font-weight:700;font-size:14px}
.contact-info .co{font-family:"Montserrat",sans-serif;font-weight:600;margin-top:12px}
.quick{position:absolute;left:460px;top:96px;list-style:none;font-size:12.5px;line-height:21px}
.field{position:absolute;top:101px;height:33px;background:#fff;color:var(--muted);font-size:11.5px;padding:0 14px;display:flex;align-items:center}
.site-footer .btn{left:611px;top:152px;width:129px;height:30px}
.to-top{position:absolute;left:1119px;top:70px;width:24px;height:24px;border-radius:50%;background:var(--green)}
.foot-rule{position:absolute;left:156px;top:256px;width:912px;height:1px;background:rgba(255,255,255,.35)}
.copyright{position:absolute;left:156px;top:278px;font-size:11.5px}
.get-social{position:absolute;left:874px;top:274px;display:flex;align-items:center;gap:12px;font-family:"Montserrat",sans-serif;font-weight:600;font-size:12px;color:var(--green)}
</style>
</head>
<body>

<header class="site-header">
  <div class="abs brand">
    <span class="brand-mark"></span>
    <div>
      <div class="brand-name">PLWT Advisory</div>
      <div class="brand-tag">Building HR Competencies in Business Leaders</div>
    </div>
  </div>
  <div class="abs call">Call Us:
    <svg width="14" height="18" viewBox="0 0 14 18"><rect x="1" y="1" width="12" height="16" rx="2" fill="var(--green)"/><rect x="3" y="3" width="8" height="10" fill="#fff"/></svg>
    <b>555-014-7890</b></div>
  <div class="abs social header-social"><span></span><span class="on"></span><span></span></div>
  <nav class="abs nav">
    <a class="active" style="left:0">Home</a>
    <a style="left:74px">My Approach</a>
    <a style="left:200px">My Services</a>
    <a style="left:315px">Dana</a>
    <a style="left:394px">Contact Me</a>
  </nav>
</header>

<section class="abs hero">
  <div class="hero-art" role="img" aria-label="Stacked colourful clay cubes, each marked with a simple person figure, on a wooden table"></div>
  <h1>Are You Receiving the Best<br><strong>“Return on Investment”</strong> From Your<br>Human Capital?</h1>
  <a class="btn">Contact Us</a>
  <span class="arrow arrow-left"><svg width="10" height="10" viewBox="0 0 10 10"><path d="M7 1 3 5l4 4" stroke="#fff" stroke-width="1.6" fill="none"/></svg></span>
  <span class="arrow arrow-right"><svg width="10" height="10" viewBox="0 0 10 10"><path d="M3 1l4 4-4 4" stroke="#fff" stroke-width="1.6" fill="none"/></svg></span>
</section>

<section class="approach">
  <div class="abs eyebrow approach-label">My Approach</div>
  <h2 class="abs approach-title">Entrepreneurs are<br>innovative risk-taking business leaders.</h2>
  <p class="abs body-copy approach-p1">I consult with small to medium sized business owners to support, complement or develop their skill set in talent management.</p>
  <h3 class="abs approach-sub">Build Your Human Resources Competencies!</h3>
  <p class="abs body-copy approach-p2">I consult with small to medium sized business<br>owners to support, complement or develop their skill set in talent management. My human resources<br>consulting services focus on ...</p>
  <a class="btn btn-outline">Discover My Focus</a>
  <div class="abs portrait" role="img" aria-label="Portrait photo of the consultant in front of a brick wall and window"></div>
</section>

<section class="services">
  <div class="abs eyebrow services-label">My Services</div>
  <div class="abs tabs">
    <div class="tab">Hr and Business Consultant</div>
    <div class="tab active">Trainer and Facilitator</div>
    <div class="tab">Hr Project Manager</div>
  </div>
  <h2 class="abs topics-title">Topics relevant to your<br>organization – as you need it.</h2>
  <ul class="abs topics">
    <li><svg width="9" height="8" viewBox="0 0 9 8"><path d="M1 4l2.5 2.5L8 1" stroke="var(--muted)" stroke-width="1.4" fill="none"/></svg>HR's Impact on the Bottom Line</li>
    <li><svg width="9" height="8" viewBox="0 0 9 8"><path d="M1 4l2.5 2.5L8 1" stroke="var(--muted)" stroke-width="1.4" fill="none"/></svg>Human Capital Strategies</li>
    <li><svg width="9" height="8" viewBox="0 0 9 8"><path d="M1 4l2.5 2.5L8 1" stroke="var(--muted)" stroke-width="1.4" fill="none"/></svg>Employment Law</li>
    <li><svg width="9" height="8" viewBox="0 0 9 8"><path d="M1 4l2.5 2.5L8 1" stroke="var(--muted)" stroke-width="1.4" fill="none"/></svg>Leadership Competencies</li>
    <li><svg width="9" height="8" viewBox="0 0 9 8"><path d="M1 4l2.5 2.5L8 1" stroke="var(--muted)" stroke-width="1.4" fill="none"/></svg>Vision/Mission/Value Statements</li>
    <li><svg width="9" height="8" viewBox="0 0 9 8"><path d="M1 4l2.5 2.5L8 1" stroke="var(--muted)" stroke-width="1.4" fill="none"/></svg>Performance Management</li>
    <li><svg width="9" height="8" viewBox="0 0 9 8"><path d="M1 4l2.5 2.5L8 1" stroke="var(--muted)" stroke-width="1.4" fill="none"/></svg>Organizational Design and Development</li>
    <li><svg width="9" height="8" viewBox="0 0 9 8"><path d="M1 4l2.5 2.5L8 1" stroke="var(--muted)" stroke-width="1.4" fill="none"/></svg>Strategic Compensation and Rewards</li>
    <li><svg width="9" height="8" viewBox="0 0 9 8"><path d="M1 4l2.5 2.5L8 1" stroke="var(--muted)" stroke-width="1.4" fill="none"/></svg>Employee Engagement</li>
    <li><svg width="9" height="8" viewBox="0 0 9 8"><path d="M1 4l2.5 2.5L8 1" stroke="var(--muted)" stroke-width="1.4" fill="none"/></svg>Organizational Culture</li>
    <li><svg width="9" height="8" viewBox="0 0 9 8"><path d="M1 4l2.5 2.5L8 1" stroke="var(--muted)" stroke-width="1.4" fill="none"/></svg>Interviewing</li>
    <li><svg width="9" height="8" viewBox="0 0 9 8"><path d="M1 4l2.5 2.5L8 1" stroke="var(--muted)" stroke-width="1.4" fill="none"/></svg>Communication</li>
    <li><svg width="9" height="8" viewBox="0 0 9 8"><path d="M1 4l2.5 2.5L8 1" stroke="var(--muted)" stroke-width="1.4" fill="none"/></svg>Workplace Etiquette</li>
    <li><svg width="9" height="8" viewBox="0 0 9 8"><path d="M1 4l2.5 2.5L8 1" stroke="var(--muted)" stroke-width="1.4" fill="none"/></svg>Managing Multiple Generations</li>
    <li><svg width="9" height="8" viewBox="0 0 9 8"><path d="M1 4l2.5 2.5L8 1" stroke="var(--muted)" stroke-width="1.4" fill="none"/></svg>Avoiding Unionization</li>
    <li><svg width="9" height="8" viewBox="0 0 9 8"><path d="M1 4l2.5 2.5L8 1" stroke="var(--muted)" stroke-width="1.4" fill="none"/></svg>And more...</li>
  </ul>
  <a class="btn services-btn">Contact Us</a>
  <div class="abs services-art" role="img" aria-label="Isometric illustration of business people climbing a growing stack of orange and purple bar blocks on a light blue ground"></div>
</section>

<div class="abs map" role="img" aria-label="World map in light grey with a location pin marking the office"></div>

<footer class="abs site-footer">
  <div class="foot-h" style="left:156px">Contact info</div>
  <div class="contact-info">
    <div class="phone">Call Us: 555.014.2722</div>
    <div>E. DWhitlow@PLWTAdvisory.com</div>
    <div class="co">Dana Whitlow ~ PLWT Advisory, LLC</div>
    <div>Suite 210, 48 Larkspur Ave,<br>Denver CO - 80202</div>
  </div>
  <div class="foot-h" style="left:460px">Quick Link</div>
  <ul class="quick">
    <li>Home</li><li>My Approach</li><li>My Services</li><li>Dana</li><li>Contact Me</li>
  </ul>
  <div class="foot-h" style="left:611px">Join Dana's Mailing List!</div>
  <div class="field" style="left:611px;width:209px">Full Name</div>
  <div class="field" style="left:835px;width:208px">Enter Your Email ....</div>
  <a class="btn">Subscribe Now!</a>
  <span class="to-top"><svg width="24" height="24" viewBox="0 0 24 24"><path d="M8 14l4-4 4 4" stroke="#fff" stroke-width="1.8" fill="none"/></svg></span>
  <div class="foot-rule"></div>
  <div class="copyright">© 2018 Dana Whitlow ~ PLWT Advisory, LLC. All Right Reserved</div>
  <div class="get-social">Get Social: <span class="social"><span></span><span class="on"></span><span></span></span></div>
</footer>

</body>
</html>
```